Copper Ridge Business Cards For New Startup

I am looking for you to design some business cards for a new startup https://copperridgehub.example. I have supplied logo, brand guidelines and our signatures as a guide.

We need this to reflect the brand guidelines and the website for brand consistency,

What is Copper Ridge?

Mallorca's Business Growth Community
Join your new business community full of passionate entrepreneurs who
love to solve problems and help each other grow together!

Any questions you can ask.

Target Market(s)

Business to Business

Contact Information for Business Card

These are attached (signatures) to the job

Font styles to use
Other font styles liked:
• Open Sans

Requirements
Must have
• Match design guidelines
Nice to have
• Photos of our faces so people remember us

```html
<!DOCTYPE html>
<html lang="en">
<head>
<meta charset="utf-8">
<title>Copper Ridge – Business Card</title>
<link href="https://fonts.googleapis.com/css2?family=Open+Sans:wght@400;600;700&display=swap" rel="stylesheet">
<style>
  :root {
    --olive: #65692f;
    --mist: #e8f3f2;
    --ink: #2b2b2b;
    --paper: #eaf4f3;
    --backdrop: #d8d2c6;
  }
  * { margin: 0; padding: 0; box-sizing: border-box; }
  html, body { width: 900px; height: 1200px; overflow: hidden; }
  body {
    background: var(--backdrop);
    font-family: "Open Sans", sans-serif;
    position: relative;
  }
  .card {
    position: absolute;
    left: 86px;
    width: 736px;
    height: 430px;
    overflow: hidden;
    box-shadow: 0 4px 14px rgba(0,0,0,0.25);
  }
  .card--front { top: 136px; background: var(--mist); }
  .card--back { top: 634px; background: var(--olive); }

  .front-band { position: absolute; inset: 0; }

  .portrait {
    position: absolute;
    left: 30px; top: 31px;
    width: 206px; height: 206px;
    border-radius: 50%;
    border: 6px solid var(--olive);
    background: radial-gradient(circle at 50% 40%, #c9a58c 0 30%, #9c8f80 55%, #dfe3e0 100%);
  }
  .identity { position: absolute; left: 254px; top: 82px; color: var(--ink); }
  .identity__name { font-size: 31px; font-weight: 700; line-height: 40px; }
  .identity__role { font-size: 22px; font-weight: 400; line-height: 32px; }

  .contact { position: absolute; display: flex; align-items: center; color: #fff; font-size: 22px; }
  .contact__icon {
    width: 42px; height: 42px; border-radius: 50%;
    border: 2px solid #fff; background: var(--olive);
    display: flex; align-items: center; justify-content: center;
    margin-right: 14px;
  }
  .contact--phone { left: 166px; top: 249px; }
  .contact--email { left: 99px; top: 298px; }
  .contact--web { left: 42px; top: 354px; }

  .brand-mark {
    position: absolute; display: flex; flex-direction: column; align-items: center;
    color: var(--paper); font-weight: 600;
  }
  .brand-mark__circle { border: 3px solid var(--paper); border-radius: 50%; }
  .brand-mark--front { right: 40px; top: 250px; font-size: 18px; }
  .brand-mark--front .brand-mark__circle { width: 100px; height: 100px; margin-bottom: 10px; }

  .brand-lockup {
    position: absolute; left: 72px; top: 122px;
    display: flex; align-items: center; color: var(--paper);
  }
  .brand-lockup__circle {
    width: 128px; height: 124px; border: 3px solid var(--paper);
    border-radius: 50%; margin-right: 42px;
  }
  .brand-lockup__name { font-size: 62px; font-weight: 600; letter-spacing: 1px; }

  .social { position: absolute; left: 206px; top: 346px; display: flex; gap: 22px; }
  .social__dot { width: 48px; height: 48px; border-radius: 50%; background: var(--paper); }
</style>
</head>
<body>
  <section class="card card--front">
    <svg class="front-band" width="736" height="430" viewBox="0 0 736 430" aria-hidden="true">
      <path d="M0,430 C120,330 300,190 500,188 C600,187 690,205 736,225 L736,430 Z" fill="var(--olive)"/>
    </svg>
    <div class="portrait" role="img" aria-label="Portrait photo of Marcus Hale"></div>
    <div class="identity">
      <h1 class="identity__name">Marcus Hale</h1>
      <p class="identity__role">Founder &amp; Growth Hacker | Copper Ridge</p>
    </div>

    <div class="contact contact--phone">
      <span class="contact__icon">
        <svg width="16" height="24" viewBox="0 0 16 24"><rect x="1.5" y="1.5" width="13" height="21" rx="2" fill="none" stroke="#fff" stroke-width="2"/><line x1="6" y1="19" x2="10" y2="19" stroke="#fff" stroke-width="2"/></svg>
      </span>
      <span>+34 611 482 907</span>
    </div>
    <div class="contact contact--email">
      <span class="contact__icon">
        <svg width="22" height="16" viewBox="0 0 22 16"><rect x="0" y="0" width="22" height="16" rx="1" fill="#fff"/><path d="M1 1 L11 9 L21 1" fill="none" stroke="var(--olive)" stroke-width="1.6"/></svg>
      </span>
      <span>mh@copperridgehub.example</span>
    </div>
    <div class="contact contact--web">
      <span class="contact__icon">
        <svg width="22" height="22" viewBox="0 0 22 22" fill="none" stroke="#fff" stroke-width="1.6"><circle cx="11" cy="11" r="9.5"/><ellipse cx="11" cy="11" rx="4.5" ry="9.5"/><line x1="1.5" y1="11" x2="20.5" y2="11"/><line x1="3" y1="6" x2="19" y2="6"/><line x1="3" y1="16" x2="19" y2="16"/></svg>
      </span>
      <span>copperridgehub.example</span>
    </div>

    <div class="brand-mark brand-mark--front">
      <span class="brand-mark__circle"></span>
      <span>Copper Ridge</span>
    </div>
  </section>

  <section class="card card--back">
    <div class="brand-lockup">
      <span class="brand-lockup__circle"></span>
      <span class="brand-lockup__name">COPPER RIDGE</span>
    </div>
    <div class="social" aria-label="Social channels">
      <span class="social__dot"></span>
      <span class="social__dot"></span>
      <span class="social__dot"></span>
      <span class="social__dot"></span>
      <span class="social__dot"></span>
    </div>
  </section>
</body>
</html>
```